Monument sign* - Law Firm

*I am installing a monument sign that has LED, as well as backlit elements. I am seeking help in designing the backlit portion of the sign. The Backlit sign will be 12’ x 4’.

We are looking for a classic, yet eye-catching sign to help new and current clients find our firm as well as bring in future clients. One of our goals is that people who drive by on a regular basis remember our sign (and us) for any future legal need.

Target Market(s)

Current and future clientele

Industry/Entity Type

Law Firm

Font styles to use
Serif
Sans Serif

Colors
b1b1b1
333333

Requirements
Must have
• Business name: Hartwell Law Firm, Inc.
• Website: www.hartwelllawfirm-example.com
• Telephone: (555)274-1936
• Our firm's logo
Nice to have
• Color preference is black, taupe, and white. A photo for reference of the office coloring is uploaded.
• We currently have an established logo which our firm has been using for more than 10 years. Our logo has been used in advertising, commercials, letterhead, and on-site. We are looking to transition from brown/rust/cream to the black/taupe/white color scheme.
Should not have
• Cheesy slogans; character designs; directions; additional symbols outside of the firm's logo.

```html
<!DOCTYPE html>
<html lang="en">
<head>
<meta charset="utf-8">
<title>Hartwell Law Firm, Inc. — Backlit Sign</title>
<link rel="stylesheet" href="https://fonts.googleapis.com/css2?family=Tinos:wght@400;700&display=swap">
<style>
  :root {
    --canvas: #e6e6e6;
    --ink: #221c1b;
    --band-dark: #2b2322;
    --taupe: #cbbba3;
    --taupe-deep: #b5a286;
    --cream-top: #ffffff;
    --cream-bottom: #d9cebd;
    --photo-sky: #eef0ee;
    --photo-wall: #a39c8e;
    --photo-lawn: #4f8a34;
    --white: #ffffff;
  }
  * { margin: 0; padding: 0; box-sizing: border-box; }
  html, body { width: 1200px; height: 1000px; overflow: hidden; }
  body { background: var(--canvas); font-family: "Tinos", "Times New Roman", serif; }

  .sign {
    position: absolute; left: 60px; top: 321px;
    width: 1080px; height: 357px; overflow: hidden;
    background: linear-gradient(180deg, var(--cream-top) 0%, var(--cream-bottom) 100%);
    box-shadow: 0 18px 24px -14px rgba(0,0,0,.45);
  }
  .sign__band {
    position: absolute; left: 0; top: 236px; width: 100%; height: 61px;
    background: var(--band-dark);
  }
  .sign__footer {
    position: absolute; left: 0; top: 297px; width: 100%; height: 60px;
    background: var(--taupe);
  }
  .sign__divider {
    position: absolute; inset: 0; background: var(--band-dark);
    clip-path: polygon(851px 0, 1080px 0, 1080px 357px, 814px 357px);
  }
  .sign__photo {
    position: absolute; inset: 0;
    background: linear-gradient(180deg, var(--photo-sky) 0%, var(--photo-wall) 22%, #8e877a 70%, var(--photo-lawn) 82%, #3f7a2a 100%);
    clip-path: polygon(861px 0, 1080px 0, 1080px 357px, 824px 357px);
  }

  .text-area { position: absolute; left: 0; top: 0; width: 823px; height: 100%; }
  .logo {
    position: absolute; left: 342px; top: 25px; width: 153px; height: 126px;
    background: var(--white); box-shadow: 0 1px 3px rgba(0,0,0,.25);
    display: flex; align-items: center; justify-content: center; gap: 8px;
  }
  .logo__square { width: 22px; height: 22px; background: var(--taupe-deep); }
  .logo__name { font-size: 22px; font-weight: 700; color: var(--ink); }

  .firm-name {
    position: absolute; left: 0; width: 100%; top: 165px;
    text-align: center; font-size: 58px; font-weight: 700; color: var(--ink);
    text-transform: uppercase; letter-spacing: 0.5px; line-height: 1;
  }
  .phone {
    position: absolute; left: 0; width: 100%; top: 236px; height: 61px;
    display: flex; align-items: center; justify-content: center; gap: 12px;
    font-size: 39px; color: var(--white); letter-spacing: 1px;
  }
  .phone__icon { width: 30px; height: 30px; }
  .website {
    position: absolute; left: 0; width: 100%; top: 297px; height: 60px;
    display: flex; align-items: center; justify-content: center;
    font-size: 30px; font-weight: 700; color: var(--ink); letter-spacing: 2px;
  }
</style>
</head>
<body>
  <div class="sign">
    <div class="sign__band"></div>
    <div class="sign__footer"></div>
    <div class="sign__divider"></div>
    <div class="sign__photo" role="img" aria-label="Photo of a stucco cottage with a steep gabled roof, dark front door and green lawn"></div>

    <div class="text-area">
      <div class="logo">
        <span class="logo__square"></span>
        <span class="logo__name">Hartwell</span>
      </div>
      <div class="firm-name">Hartwell Law Firm, Inc.</div>
      <div class="phone">
        <svg class="phone__icon" viewBox="0 0 30 30" aria-hidden="true">
          <circle cx="15" cy="15" r="15" fill="#b5a286"/>
          <path d="M10.5 8.5c.8-.6 1.6-.4 2 .3l1.3 2.4c.3.6.2 1.2-.3 1.6l-1 .8c.7 1.6 2 2.9 3.6 3.7l.8-1c.4-.5 1.1-.6 1.6-.3l2.4 1.3c.7.4.9 1.2.3 2l-1 1.2c-.6.7-1.6.9-2.5.6-4-1.4-7-4.5-8.4-8.5-.3-.9-.1-1.9.6-2.5z" fill="#ffffff"/>
        </svg>
        <span>(555)274-1936</span>
      </div>
      <div class="website">www.hartwelllawfirm-example.com</div>
    </div>
  </div>
</body>
</html>
```